Web Design Project

Dear designer(s),

I need a design for a shop who's specialized into...

-Material to fix or do tailor made clothing (cloth, buttons, zippers etc)
-Curtains (static/pull-up)
-Blinds (plastic/wood)

that kind of stuff.

Good thing is that I can provide a lot of pretty photo's to work with. I have 3.5 Gigabyte of 300-1200 dpi photo's altho I converted most of them to 72dpi for your convenience (75Mb).

You can download the working material from this quellbin link:

http://files.quellbin.net/u/31920586/Velunor.zip

this is an updated file, it contains the dutch menu items to use in your design

http://files.quellbin.net/u/31920586/Velunor_Content.txt

Notice: take your time to come up with something nice. I prefer 1 or 2 designs from a designer that has been thinked of, than 5 quick ones.
Updates

Thank you for those who posted designs already but I want to clarify something.

As I mentioned it's a shop, that's a physical shop and not a webshop.

So you can safe some time and skip drawing the shopping cart icons, shop items on the homepage and other shop related things.

They don't want to start online reselling as they already spend most of their time in their shop to catch up with all orders.

Keep up the good work!

Industry/Entity Type

Clothing

Requirements
Nice to have
• Maybe the hi-res pictures can be used as background ratotor that appears left/right next to the centered website content?

Since there is a lot of material each section might have his topic linked set of thumbnails that opens a bigger image on clicking?

```html
<!DOCTYPE html>
<html lang="nl">
<head>
<meta charset="utf-8">
<title>Velunor</title>
<link href="https://fonts.googleapis.com/css2?family=Roboto+Condensed:wght@300;400&display=swap" rel="stylesheet">
<style>
:root{
  --blue:#1279bf;
  --blue-dark:#0d69a8;
  --ink:#6a6a6a;
  --body:#929292;
  --rule:#d9d9d9;
  --footer:#8c8c8c;
  --white:#ffffff;
}
*{margin:0;padding:0;box-sizing:border-box}
html,body{width:1041px;height:1200px;overflow:hidden}
body{position:relative;font-family:"Roboto Condensed",sans-serif;font-weight:300;color:var(--body);
  background:linear-gradient(#e9e9e9 551px,#f6f6f6 800px,#ffffff 1143px)}
.abs{position:absolute}
.hero{left:0;top:0;width:1041px;height:551px;
  background:linear-gradient(100deg,#d9d6d2 0%,#ece9e5 30%,#f4f1ec 55%,#e5dfd8 80%,#cfc8c0 100%)}
.logo{left:113px;top:0;width:232px;height:91px;background:var(--white);display:flex;align-items:center;padding-left:16px;gap:8px}
.logo .dot{width:12px;height:12px;background:var(--blue);border-radius:50%}
.logo .name{font-size:26px;font-weight:400;color:var(--blue)}
.logo .url{position:absolute;right:12px;bottom:10px;font-size:12px;color:#7a7a7a}
.social{top:14px;left:862px;display:flex;gap:9px}
.social span{width:12px;height:12px;border-radius:50%;background:#9a9a9a}
.nav{left:449px;top:46px;width:592px;height:46px}
.nav ul{position:absolute;left:30px;top:0;height:46px;display:flex;align-items:center;list-style:none}
.nav li{font-size:12.5px;font-weight:400;color:var(--white);padding:0 11px;position:relative;text-transform:uppercase}
.nav li+li::before{content:"";position:absolute;left:0;top:4px;width:1px;height:6px;background:#8cc3e8}
.nav li.current{background:var(--white);color:var(--blue);height:48px;margin-top:-4px;line-height:52px;padding:0 12px}
.claim{left:0;top:229px;width:541px;height:123px;background:rgba(255,255,255,.45)}
.claim h1{position:absolute;left:113px;top:16px;font-weight:300;font-size:36px;line-height:41px;color:#5c5c5c;text-transform:uppercase}
.claim .bars{position:absolute;left:113px;top:104px;display:flex;gap:3px}
.claim .bars i{width:57px;height:2px;background:#6a6a6a}
.claim .bars i:first-child{background:var(--blue)}
.card{top:470px;width:263px;height:359px;border:3px solid #dcdcdc;background:linear-gradient(#f1f1f1,#fafafa)}
.card h2{position:absolute;left:10px;top:10px;font-weight:300;font-size:29px;line-height:27px;text-transform:uppercase;color:#7a7a7a}
.card h2 b{font-weight:300;color:var(--blue);display:block}
.card .photo{position:absolute;left:10px;top:73px;width:237px;height:174px}
.card p{position:absolute;left:10px;top:256px;width:240px;font-size:11.2px;line-height:13.6px}
.btn{position:absolute;height:22px;padding:0 6px 0 13px;background:var(--blue);color:var(--white);font-size:11.5px;font-weight:400;line-height:22px}
.btn::before{content:"";position:absolute;left:0;top:6px;border:5px solid transparent;border-left:5px solid var(--white)}
.card .btn{right:13px;top:318px}
.section-title{font-weight:300;font-size:23px;color:var(--ink)}
.section-title b{font-weight:300;color:var(--blue)}
.rule{height:1px;background:var(--blue)}
.rule::after{content:"";position:absolute;right:0;top:-1px;width:4px;height:3px;background:var(--blue)}
.text{font-size:11.2px;line-height:13.6px}
.thumb{left:639px;width:282px;height:104px;border:1px solid #e3e3e3;background:var(--white)}
.thumb div{position:absolute;left:7px;top:7px;right:7px;bottom:7px}
footer{left:0;top:1143px;width:1041px;height:57px;background:var(--footer);color:var(--white)}
footer .legal{position:absolute;left:114px;top:20px;font-size:12px;font-weight:400;display:flex;align-items:center;gap:7px}
footer .legal i{width:4px;height:4px;background:var(--white)}
footer .brand{position:absolute;left:800px;top:16px;display:flex;align-items:center;gap:6px;font-size:18px;font-weight:400;color:#d6d6d6}
footer .brand span{width:9px;height:9px;border-radius:50%;background:#d6d6d6}
</style>
</head>
<body>
<div class="abs hero" role="img" aria-label="Bright living room with white venetian blinds, white sofa, arc floor lamp and a vase of flowers"></div>

<div class="abs logo"><span class="dot"></span><span class="name">Velunor</span><span class="url">www.velunor.be</span></div>
<div class="abs social"><span></span><span></span><span></span></div>

<nav class="abs nav">
  <svg class="abs" style="left:0;top:0" width="592" height="46"><polygon points="30,0 592,0 592,46 0,46" fill="#1279bf"/></svg>
  <ul>
    <li class="current">Home</li><li>Tafellinnen</li><li>Decoration cloth</li><li>Optreksystemen</li><li>Contact</li>
  </ul>
</nav>

<div class="abs claim">
  <h1>Client experience<br>is very important for us</h1>
  <div class="bars"><i></i><i></i><i></i></div>
</div>

<section class="abs card" style="left:117px">
  <h2><b>Fresh</b>Solutions</h2>
  <div class="photo" role="img" aria-label="Dining room with dark roman blinds" style="background:linear-gradient(135deg,#d8d4cf,#8a7a70 60%,#4a3e38)"></div>
  <p>Lorem ipsum dolor sit amet, consectetuer adipiscing elit, sed diam nonummy nibh euismod tincidunt ut laoreet dolore magna aliquam erat volutpat. Ut wisi enim ad minim veniam.</p>
  <span class="btn">Read More</span>
</section>
<section class="abs card" style="left:390px">
  <h2><b>New</b>Technologies</h2>
  <div class="photo" role="img" aria-label="White kitchen with light blue roller blinds" style="background:linear-gradient(160deg,#c7d9e8,#eef2f3 55%,#9aa3ab)"></div>
  <p>Lorem ipsum dolor sit amet, consectetuer adipiscing elit, sed diam nonummy nibh euismod tincidunt ut laoreet dolore magna aliquam erat volutpat. Ut wisi enim ad minim veniam.</p>
  <span class="btn">Read More</span>
</section>
<section class="abs card" style="left:664px">
  <h2><b>Eco</b>Materials</h2>
  <div class="photo" role="img" aria-label="Attic living room with pleated skylight blinds" style="background:linear-gradient(170deg,#e9ebe8,#d8d4cc 60%,#9b8a7c)"></div>
  <p>Lorem ipsum dolor sit amet, consectetuer adipiscing elit, sed diam nonummy nibh euismod tincidunt ut laoreet dolore magna aliquam erat volutpat. Ut wisi enim ad minim veniam.</p>
  <span class="btn">Read More</span>
</section>

<h2 class="abs section-title" style="left:114px;top:845px">Welcome To <b>Velunor</b></h2>
<div class="abs rule" style="left:114px;top:875px;width:464px"></div>
<p class="abs text" style="left:114px;top:888px;width:465px">Lorem ipsum dolor sit amet, consectetuer adipiscing elit, sed diam nonummy nibh euismod tincidunt ut laoreet dolore magna aliquam erat volutpat. Ut wisi enim ad minim veniam.Lorem ipsum dolor sit amet, consectetuer adipiscing elit, sed diam nonummy nibh euismod tincidunt ut laoreet dolore magna aliquam erat volutpat. Ut wisi enim ad minim veniam.Lorem ipsum dolor sit amet, consectetuer adipiscing elit, sed diam nonummy nibh euismod tincidunt ut laoreet dolore magna aliquam erat volutpat. Ut wisi enim ad minim veniam.</p>
<div class="abs" style="left:215px;top:993px;width:239px;height:1px;background:var(--rule)"></div>

<h2 class="abs section-title" style="left:114px;top:1008px">Did You Know?</h2>
<div class="abs rule" style="left:114px;top:1039px;width:464px"></div>
<p class="abs text" style="left:114px;top:1052px;width:465px">Lorem ipsum dolor sit amet, consectetuer adipiscing elit, sed diam nonummy nibh euismod tincidunt ut laoreet dolore magna aliquam erat volutpat. Ut wisi enim ad minim veniam.Lorem ipsum dolor sit amet, consectetuer adipiscing elit.</p>
<span class="btn" style="left:514px;top:1092px">Read More</span>

<div class="abs" style="left:603px;top:890px;width:1px;height:231px;background:var(--rule)"></div>

<h2 class="abs section-title" style="left:627px;top:845px">Latest Projects</h2>
<div class="abs rule" style="left:627px;top:875px;width:301px"></div>
<div class="abs thumb" style="top:899px"><div role="img" aria-label="Living room with beige roman blinds and a floor lamp" style="background:linear-gradient(100deg,#6b7a80,#b99f88 45%,#e8e2d6)"></div></div>
<div class="abs thumb" style="top:1014px"><div role="img" aria-label="Room with wooden venetian blinds" style="background:linear-gradient(100deg,#e6e6e4,#b8b2aa 45%,#c79a62 70%,#8a6440)"></div></div>

<footer class="abs">
  <div class="legal">VELUNOR © 2013 <i></i> PRIVACY POLICY</div>
  <div class="brand"><span></span>Velunor</div>
</footer>
</body>
</html>
```